plumbing & gas fitting business card design

We need a business card design for a plumbing & gas fitting company. The company covers commercial, domestic and maintenance work. We would like a modern design communicating efficiency and sophistication. preferred colours would include (red grey & black) or (green grey & black). Please DO NOT include any water droplets.

Industry/Entity Type

Business

Contact Information for Business Card

Vortig Plumbing & Gas, Commercial Domestic & Maintenance, licence no. 617394K, ABN 47215830962, Phone 0417382956, Email vortigplumbingandgas@corvanet.com

```html
<!DOCTYPE html>
<html lang="en">
<head>
<meta charset="utf-8">
<title>Vortig Plumbing &amp; Gas — Business Card</title>
<link rel="stylesheet" href="https://fonts.googleapis.com/css2?family=Inter:wght@300;400&display=swap">
<style>
  :root {
    --card-bg: #8a9f9e;
    --ink: #0d0d0d;
    --ink-soft: #161616;
    --accent-red: #ff1111;
  }
  html, body {
    margin: 0;
    padding: 0;
    width: 1200px;
    height: 693px;
    overflow: hidden;
    background: var(--card-bg);
  }
  .card {
    position: relative;
    width: 1200px;
    height: 693px;
    background: var(--card-bg);
    font-family: "Inter", "Helvetica Neue", Arial, sans-serif;
    color: var(--ink);
  }
  .brand-name {
    position: absolute;
    left: 0;
    top: 41px;
    width: 1200px;
    margin: 0;
    text-align: center;
    font-size: 107px;
    font-weight: 300;
    line-height: 1;
    letter-spacing: 0.08em;
    padding-left: 0.08em;
    box-sizing: border-box;
  }
  .brand-rule {
    position: absolute;
    left: 299px;
    top: 151px;
    width: 602px;
    height: 3px;
    background: var(--ink);
  }
  .brand-trade {
    position: absolute;
    left: 0;
    top: 169px;
    width: 1200px;
    margin: 0;
    text-align: center;
    font-size: 44px;
    font-weight: 400;
    line-height: 1;
    letter-spacing: 0.38em;
    padding-left: 0.38em;
    box-sizing: border-box;
  }
  .services {
    position: absolute;
    left: 446px;
    top: 273px;
    width: 302px;
    margin: 0;
    padding: 0;
    list-style: none;
    color: var(--accent-red);
    font-size: 45px;
    font-weight: 300;
    line-height: 48px;
    letter-spacing: 0.02em;
  }
  .services .service-joined {
    text-align: justify;
    text-align-last: justify;
  }
  .contact {
    position: absolute;
    left: 68px;
    top: 489px;
    margin: 0;
    padding: 0;
    list-style: none;
    color: var(--ink-soft);
    font-size: 25px;
    font-weight: 300;
    line-height: 36px;
  }
</style>
</head>
<body>
  <main class="card">
    <h1 class="brand-name">Vortig</h1>
    <div class="brand-rule"></div>
    <p class="brand-trade">plumbing &amp; gas</p>

    <ul class="services">
      <li>Commercial</li>
      <li class="service-joined">Domestic &amp;</li>
      <li>Maintenance</li>
    </ul>

    <ul class="contact">
      <li>licence no. 617394K</li>
      <li>ABN.&nbsp; 47215830962</li>
      <li>Phone number: 0417382956</li>
      <li>Email: vortigplumbingandgas@corvanet.com</li>
    </ul>
  </main>
</body>
</html>
```